Fitness website

Website for a fitness brand (see attached specs). Design needs to be modern and vibrant with CTAs on every page. We will provide logos, images, etc but for now user placeholder text and images. For now use the name 'Veltrano Athletics' as the name to use on the design. The goal of this site is to either get people to join the gym (5 physical locations across the US); buy an online program; buy merch or supplements or sign up for the newsletter. Pleas use images from this foldeR: https://files.quorbex.net/share/8kTq27wLmZr

We will be coding this in ReactNative. Lots more work for the winner as well, this is a 1st project for us.

Target Market(s)

fitness enthusiats

Industry/Entity Type

fitness, health, wellness

Number of Pages Required

5+ page

Font styles to use
Other font styles liked:
• Lato

Colors
0054AA
0677BA
7BADD7
CADEEF
E8F1F8
0094D4
00A9DD
6FCCEA
C7EBF8
E9F6FB
00AB8E
00BBA5
67D7C9
C6EFE9
E9F9F6
EE7325
F08F49
F5BC92
FAE3D3
FDF4ED

Requirements
Must have
• must be reactive. most people will view it first on mobile
Nice to have
• video in hero section of top of home page

```html
<!DOCTYPE html>
<html lang="en">
<head>
<meta charset="utf-8">
<title>Veltrano Athletics</title>
<link href="https://fonts.googleapis.com/css2?family=Montserrat:wght@600;700;800;900&family=Lato:wght@400;700;900&display=swap" rel="stylesheet">
<style>
:root{
  --green:#1f9a3c;
  --green-dark:#167a2e;
  --yellow:#ffd200;
  --ink:#111111;
  --ink-soft:#2b2b2b;
  --cream:#f6f4e8;
  --white:#ffffff;
  --muted:#6b6b6b;
  --card:#e9e9e6;
}
*{box-sizing:border-box;margin:0;padding:0}
html,body{width:1200px;height:4136px;overflow:hidden}
body{position:relative;background:var(--cream);font-family:'Lato',sans-serif;color:var(--ink)}
h1,h2,h3,.brand,.btn,.nav a{font-family:'Montserrat',sans-serif}
.abs{position:absolute}
.btn{display:inline-flex;align-items:center;gap:10px;border-radius:30px;font-weight:800;font-size:12px;letter-spacing:.5px;padding:11px 22px;text-transform:uppercase;white-space:nowrap}
.btn-green{background:var(--green);color:var(--white)}
.btn-outline{border:2px solid var(--white);color:var(--white)}
.btn-dark{background:var(--ink);color:var(--white)}
.btn-line{border:2px solid var(--ink);color:var(--ink)}
.arrow-dot{width:18px;height:18px;border-radius:50%;background:var(--white);display:inline-block;position:relative}
.arrow-dot::after{content:"";position:absolute;left:5px;top:6px;border-left:7px solid var(--green);border-top:3px solid transparent;border-bottom:3px solid transparent}
.ph{border-radius:6px}

/* header + hero */
.hero{left:0;top:0;width:1200px;height:680px;background:radial-gradient(ellipse at 72% 40%,#6e5a48 0%,#3b3029 35%,#181513 70%,#0c0b0a 100%)}
.site-nav{left:0;top:0;width:1200px;height:72px;display:flex;align-items:center;padding:0 60px;background:rgba(0,0,0,.55)}
.brand{font-weight:900;font-size:20px;color:var(--white);letter-spacing:.5px}
.nav{display:flex;gap:24px;margin-left:auto;margin-right:20px}
.nav a{color:var(--white);font-size:11px;font-weight:700;text-decoration:none}
.icon-dot{width:22px;height:22px;border-radius:50%;border:1.5px solid var(--white);margin-right:8px}
.hero-copy{left:120px;top:180px;width:520px;color:var(--white)}
.hero-copy h1{font-size:52px;line-height:1.12;font-weight:900}
.hero-copy h1 span{color:var(--green)}
.hero-copy p{font-size:16px;line-height:1.5;margin:16px 0 26px;max-width:420px}
.play{left:1000px;top:540px;width:60px;height:60px;border-radius:50%;background:var(--white)}
.play::after{content:"";position:absolute;left:24px;top:19px;border-left:16px solid var(--ink);border-top:11px solid transparent;border-bottom:11px solid transparent}

/* about */
.about-img{left:128px;top:720px;width:540px;height:252px;background:linear-gradient(135deg,#7a5f4c,#3a3b3d 60%,#1d1d1f)}
.about-box{left:690px;top:720px;width:390px;height:252px;background:var(--yellow);padding:24px 28px}
.about-box h2{font-size:28px;line-height:1.1;font-weight:900;margin-bottom:12px}
.about-box p{font-size:10.5px;line-height:1.5;margin-bottom:8px}
.features{left:120px;top:1005px;width:960px;display:flex;justify-content:space-between}
.feature{display:flex;gap:10px;width:225px}
.feature .ic{flex:none;width:44px;height:44px;border-radius:50%;border:2px solid var(--green);position:relative}
.feature .ic::after{content:"";position:absolute;left:13px;top:10px;width:12px;height:18px;border-right:3px solid var(--green);border-bottom:3px solid var(--green);transform:rotate(40deg) scale(.7)}
.feature h3{font-size:13px;font-weight:800;margin-bottom:4px}
.feature p{font-size:9.5px;line-height:1.4;color:var(--muted)}

/* programs */
.programs{left:0;top:1130px;width:1200px;height:600px;background:var(--green)}
.programs h2{position:absolute;top:78px;width:100%;text-align:center;color:var(--white);font-size:38px;font-weight:900}
.prog-row{left:150px;top:232px;display:flex;gap:16px}
.prog{width:213px}
.prog .img{height:240px}
.prog .label{background:var(--white);text-align:center;font-family:'Montserrat',sans-serif;font-weight:800;font-size:14px;padding:11px 0}
.nav-arrow{top:372px;width:30px;height:30px;border-radius:50%;background:var(--white)}
.nav-arrow::after{content:"";position:absolute;top:10px;border-top:5px solid transparent;border-bottom:5px solid transparent}
.nav-arrow.left::after{left:10px;border-right:8px solid var(--ink)}
.nav-arrow.right::after{left:12px;border-left:8px solid var(--ink)}

/* shop */
.sec-title{font-size:36px;font-weight:900}
.shop-card{width:472px;height:236px;background:linear-gradient(120deg,#f2f2ef,#dcdcd6);border-radius:8px;overflow:hidden;display:flex}
.shop-card .img{width:236px;height:236px;flex:none}
.shop-card .txt{padding:34px 22px 0 14px}
.shop-card h3{font-size:24px;font-weight:900;margin-bottom:8px}
.shop-card p{font-size:10px;line-height:1.45;color:var(--muted);margin-bottom:16px}

/* blog */
.blog{width:306px}
.blog .img{height:262px}
.blog h3{font-size:15px;font-weight:800;line-height:1.25;margin-top:14px}

/* locations */
.loc-box{left:120px;top:2900px;width:386px}
.loc-head{background:var(--yellow);padding:14px 24px;font-family:'Montserrat',sans-serif;font-weight:900;font-size:30px}
.loc-list{background:var(--white);padding:14px 24px;list-style:none}
.loc-list li{display:flex;align-items:center;gap:12px;font-size:15px;font-weight:700;padding:9px 0;border-bottom:1px solid #eee}
.pin{width:14px;height:14px;border-radius:50% 50% 50% 0;background:var(--green);transform:rotate(-45deg)}

/* newsletter */
.watermark{left:0;top:3360px;width:1200px;text-align:center;font-family:'Montserrat',sans-serif;font-weight:900;font-size:86px;line-height:1;color:#e7e4d6;letter-spacing:1px;white-space:nowrap;overflow:hidden}
.news-top{left:0;top:3470px;width:1200px;height:90px;background:var(--green)}
.news{left:0;top:3540px;width:1200px;height:360px;background:var(--yellow)}
.athlete{left:110px;top:3250px;width:280px;height:650px;background:linear-gradient(180deg,#23252a 0%,#5a4536 40%,#c99a78 70%,#2a2a2c 100%);border-radius:140px 140px 0 0;opacity:.9}
.news-copy{left:560px;top:3620px;width:520px}
.news-copy h2{font-size:34px;font-weight:900;margin-bottom:10px}
.news-copy p{font-size:14px;margin-bottom:22px}
.subscribe{display:flex;background:var(--white);border-radius:30px;padding:5px 5px 5px 22px;width:420px;align-items:center}
.subscribe span{flex:1;font-size:12px;color:var(--muted)}

/* footer */
.footer{left:0;top:3900px;width:1200px;height:236px;background:var(--ink);color:#d8d8d8;padding:40px 120px 0}
.foot-cols{display:flex;gap:40px}
.foot-cols h4{font-family:'Montserrat',sans-serif;color:var(--white);font-size:14px;font-weight:800;margin-bottom:14px}
.foot-cols li{list-style:none;font-size:10px;margin-bottom:7px;display:flex;align-items:center;gap:7px}
.foot-cols p{font-size:10px;line-height:1.5}
.soc{width:14px;height:14px;border-radius:50%;background:var(--green)}
.foot-bottom{position:absolute;left:120px;right:120px;top:200px;border-top:1px solid #333;padding-top:10px;font-size:9px;display:flex;justify-content:space-between}
</style>
</head>
<body>

<section class="hero abs" role="img" aria-label="Two athletes training hard side by side in a gym"></section>
<header class="site-nav abs">
  <div class="brand">VELTRANO ATHLETICS</div>
  <nav class="nav"><a>HOME</a><a>ABOUT</a><a>PROGRAMS</a><a>SHOP</a><a>BLOG</a><a>LOCATION</a><a>CONTACT US</a></nav>
  <span class="icon-dot"></span><span class="icon-dot"></span>
  <span class="btn btn-green">Join Now</span>
</header>
<div class="hero-copy abs">
  <h1>Unleash Your Potential with Veltrano <span>Athletics</span></h1>
  <p>Train with elite coaches, proven programs, and a community that drives you to be your best!</p>
  <span class="btn btn-green">Explore Programs <i class="arrow-dot"></i></span>&nbsp;&nbsp;
  <span class="btn btn-outline">Find a Gym Near You <i class="arrow-dot"></i></span>
</div>
<div class="play abs"></div>

<svg class="abs" style="left:0;top:650px" width="1200" height="40" viewBox="0 0 1200 40"><path d="M0 20 L40 8 L90 22 L150 6 L210 20 L280 10 L340 24 L410 8 L470 22 L540 6 L610 20 L680 10 L740 24 L810 6 L880 20 L950 8 L1010 22 L1080 10 L1140 22 L1200 8 L1200 40 L0 40Z" fill="#f6f4e8"/></svg>

<div class="about-img abs ph" role="img" aria-label="Athlete working out in a training hall"></div>
<div class="about-box abs">
  <h2>About<br>Veltrano Athletics</h2>
  <p>At Veltrano Athletics, we believe that everyone has the power to be stronger, faster and more resilient. Our mission is simple: to provide world-class training, expert guidance and a supportive community that pushes you to peak performance, whether it is your first class or your thousandth session with us.</p>
  <p>Founded by passionate athletes and certified trainers, our gyms bring together proven methods, modern facilities and an energy you can feel.</p>
  <span class="btn btn-dark">Meet Our Coaches <i class="arrow-dot"></i></span>
</div>

<div class="features abs">
  <div class="feature"><span class="ic"></span><div><h3>Community First</h3><p>Train alongside a supportive network of motivated members.</p></div></div>
  <div class="feature"><span class="ic"></span><div><h3>Expert Coaching</h3><p>Certified coaches guide every step of the way.</p></div></div>
  <div class="feature"><span class="ic"></span><div><h3>Flexible Options</h3><p>In-person, online or hybrid plans that fit your life.</p></div></div>
  <div class="feature"><span class="ic"></span><div><h3>Premium Facilities &amp; Gear</h3><p>Cutting-edge equipment and supplements to fuel progress.</p></div></div>
</div>

<section class="programs abs">
  <svg class="abs" style="left:0;top:-16px" width="1200" height="30" viewBox="0 0 1200 30"><path d="M0 16 L60 4 L120 18 L190 6 L260 20 L330 4 L400 16 L470 6 L540 20 L610 4 L690 18 L760 6 L830 20 L900 4 L970 18 L1040 6 L1110 20 L1200 6 L1200 30 L0 30Z" fill="#1f9a3c"/></svg>
  <h2>Featured Programs</h2>
  <div class="nav-arrow left abs" style="left:76px"></div>
  <div class="nav-arrow right abs" style="left:1094px"></div>
  <div class="prog-row abs">
    <div class="prog"><div class="img" role="img" aria-label="Masters athlete lifting" style="background:linear-gradient(160deg,#8b7766,#3c3835)"></div><div class="label">Masters</div></div>
    <div class="prog"><div class="img" role="img" aria-label="Functional fitness class" style="background:linear-gradient(160deg,#9aa0a6,#3f4449)"></div><div class="label">Functional Fitness</div></div>
    <div class="prog"><div class="img" role="img" aria-label="Competitive athlete training" style="background:linear-gradient(160deg,#7c8790,#2e3338)"></div><div class="label">Competitive</div></div>
    <div class="prog"><div class="img" role="img" aria-label="Healthy meal bowl" style="background:linear-gradient(160deg,#8fae5a,#3e6b2c)"></div><div class="label">Nutrition</div></div>
  </div>
  <span class="btn btn-outline abs" style="left:520px;top:540px">Explore Programs <i class="arrow-dot"></i></span>
  <svg class="abs" style="left:0;top:586px" width="1200" height="30" viewBox="0 0 1200 30"><path d="M0 0 L1200 0 L1200 14 L1130 26 L1060 12 L990 24 L920 10 L850 26 L780 12 L710 24 L640 10 L570 26 L500 12 L430 24 L360 10 L290 26 L220 12 L150 24 L80 10 L0 22Z" fill="#1f9a3c"/></svg>
</section>

<h2 class="sec-title abs" style="left:120px;top:1836px">Shop Veltrano Gear + Supplements</h2>
<span class="btn btn-line abs" style="left:960px;top:1840px">View All</span>
<div class="shop-card abs" style="left:120px;top:1912px"><div class="img" role="img" aria-label="Water bottle and yoga mat" style="background:linear-gradient(135deg,#d7e2a8,#8fb34c)"></div><div class="txt"><h3>Merch</h3><p>Branded apparel and gear built for hard training and everyday comfort.</p><span class="btn btn-green">Shop Now <i class="arrow-dot"></i></span></div></div>
<div class="shop-card abs" style="left:608px;top:1912px"><div class="img" role="img" aria-label="Supplement capsules" style="background:linear-gradient(135deg,#e9f3f3,#7fd0d3)"></div><div class="txt"><h3>Supplements</h3><p>Clean formulas to support energy, recovery and lean muscle growth.</p><span class="btn btn-green">Shop Now <i class="arrow-dot"></i></span></div></div>
<div class="shop-card abs" style="left:120px;top:2164px"><div class="img" role="img" aria-label="Ab roller and dumbbells" style="background:linear-gradient(135deg,#c9d3e6,#2d56a8)"></div><div class="txt"><h3>Equipment</h3><p>Durable tools for home workouts, from rollers to free weights.</p><span class="btn btn-green">Shop Now <i class="arrow-dot"></i></span></div></div>
<div class="shop-card abs" style="left:608px;top:2164px"><div class="img" role="img" aria-label="Training apparel and accessories" style="background:linear-gradient(135deg,#e4e4e4,#6d6d6d)"></div><div class="txt"><h3>Apparel</h3><p>Performance clothing that moves with you through every session.</p><span class="btn btn-green">Shop Now <i class="arrow-dot"></i></span></div></div>

<h2 class="sec-title abs" style="left:120px;top:2466px">Latest Blog &amp; Resources</h2>
<span class="btn btn-green abs" style="left:930px;top:2470px">View All Blogs</span>
<div class="blog abs" style="left:120px;top:2540px"><div class="img ph" role="img" aria-label="Athlete performing a barbell jerk" style="background:linear-gradient(160deg,#8a6a54,#2f2a27)"></div><h3>How to Fix the Dreaded Elbow Rebend in Your Jerk</h3></div>
<div class="blog abs" style="left:447px;top:2540px"><div class="img ph" role="img" aria-label="Athlete doing rope climbs in a gym" style="background:linear-gradient(160deg,#9ea3a8,#3a3d41)"></div><h3>Tips To Avoid Injury During Workouts</h3></div>
<div class="blog abs" style="left:774px;top:2540px"><div class="img ph" role="img" aria-label="Runner on a track" style="background:linear-gradient(160deg,#e8e8e4,#8e9398)"></div><h3>Maximize Your Potential as a Functional Fitness Masters Athlete</h3></div>

<div class="loc-box abs">
  <div class="loc-head">Our Locations</div>
  <ul class="loc-list">
    <li><span class="pin"></span>San Diego (HQ)</li>
    <li><span class="pin"></span>Boston</li>
    <li><span class="pin"></span>Miami</li>
    <li><span class="pin"></span>Seattle</li>
    <li><span class="pin"></span>NYC</li>
  </ul>
</div>
<div class="abs ph" role="img" aria-label="City skyline across the water" style="left:532px;top:2900px;width:548px;height:300px;background:linear-gradient(180deg,#7fb3e2 0%,#b9d6ef 55%,#5e7f97 70%,#2f5168 100%)"></div>

<div class="watermark abs">VELTRANO ATHLETICS</div>
<div class="news-top abs"></div>
<div class="news abs"></div>
<div class="athlete abs" role="img" aria-label="Athlete holding a barbell overhead"></div>
<div class="news-copy abs">
  <h2>Stay Connected with Veltrano</h2>
  <p>Get exclusive workouts, nutrition advice, and updates.</p>
  <div class="subscribe"><span>Enter Your Email</span><span class="btn btn-green" style="flex:none">Subscribe <i class="arrow-dot"></i></span></div>
</div>

<footer class="footer abs">
  <div class="foot-cols">
    <div style="width:210px"><h4>VELTRANO ATHLETICS</h4><p>At Veltrano Athletics, we believe that everyone has the power to be stronger, faster and more resilient through expert guidance and community.</p></div>
    <div style="width:180px"><h4>Contact Us</h4><ul><li>(555) 014-2298</li><li>hello@veltranoathletics.com</li></ul></div>
    <div><h4>Main Link</h4><ul><li>Home</li><li>About</li><li>Programs</li><li>Shop</li><li>Blog</li><li>Contact Us</li></ul></div>
    <div><h4>Our Location</h4><ul><li>San Diego (HQ)</li><li>Boston</li><li>Miami</li><li>Seattle</li><li>NYC</li></ul></div>
    <div><h4>Shop</h4><ul><li>Merch</li><li>Supplements</li><li>Equipment</li><li>Apparel</li><li>Programs</li></ul></div>
    <div><h4>Follow Us</h4><ul><li><span class="soc"></span>Feed</li><li><span class="soc"></span>Photos</li><li><span class="soc"></span>Videos</li><li><span class="soc"></span>Updates</li></ul></div>
  </div>
  <div class="foot-bottom"><span>© 2025 Veltrano Athletics All Rights Reserved</span><span>Privacy &nbsp;|&nbsp; Cookies &nbsp;|&nbsp; Conditions</span></div>
</footer>

</body>
</html>
```